New Corporate website more focused on funnel and great design

Our company, Bold Harbor needs a new website to look like it's from 2021. We work with large businesses in the corporte world and need to reflect that we are professional, focused on our clients, and trsutworthy. It should include some/most of the components from our current site: boldharbor.com but should focus more about getting people to optin to out free downloads, which can be found on this page: https://www.boldharbor.com/get-started-with-a-prep-session/ and this page: https://www.boldharbor.com/team-onboarding/

Our new website should do a better job at explaining what we do, who we serve, and how we fix their problems of onboarding new leaders. Feel free to use dummy text if you are not sure what to put in for certain sections. I also would like to point out that most of the audiance is older, so we don't need anything too younge and flashy, or that is hard it use. it should have big clear fonts, plently of contrast, and work well for poeple who are not good at using the internet. Please use the colors of the logo, and you can add another color or two if you think it's fits

Industry/Entity Type

business consulting

Number of Pages Required

2 page

Font styles to use
Sans Serif

Requirements
Must have
• corporate feel, look professional, focus on getting new leads
Should not have
• cute or children feel

```html
<!DOCTYPE html>
<html lang="en">
<head>
<meta charset="utf-8">
<title>Bold Harbor — Stronger Starts Sooner</title>
<link href="https://fonts.googleapis.com/css2?family=Lato:wght@400;700;900&family=Montserrat:ital,wght@0,300;0,400;0,500;0,600;0,700;0,800;1,300;1,400&display=swap" rel="stylesheet">
<style>
:root{
  --blue:#1b5c9e;
  --blue-dark:#124a82;
  --green:#8dc13f;
  --ink:#2f2f2f;
  --body:#7a7a7a;
  --light:#f2f2f2;
  --line:#d6d6d6;
  --footer:#2b2b2b;
  --white:#ffffff;
}
*{box-sizing:border-box;margin:0;padding:0}
html,body{width:1200px;height:5080px;overflow:hidden}
body{font-family:"Montserrat",sans-serif;color:var(--ink);background:var(--white);position:relative}
section,header,footer{position:absolute;left:0;width:1200px;overflow:hidden}
.abs{position:absolute}
.eyebrow{font-family:"Lato",sans-serif;color:var(--blue);font-size:23px;font-weight:400}
.title{font-family:"Lato",sans-serif;color:var(--ink);font-size:42px;font-weight:400}
.center{text-align:center;left:0;width:1200px}
.btn{position:absolute;display:flex;align-items:center;justify-content:center;background:var(--green);color:#fff;border-radius:30px;font-size:16px;font-weight:500;text-transform:uppercase;letter-spacing:.2px}

/* hero */
.hero{top:0;height:687px}
.hero-photo{position:absolute;inset:0;background:radial-gradient(ellipse at 62% 40%,#7d8794 0%,#4d5865 35%,#2d3640 70%,#1e252d 100%)}
.brand{position:absolute;display:flex;align-items:center;gap:12px;color:#fff}
.brand-box{width:44px;height:44px;border:3px solid #fff}
.brand-name{font-size:33px;font-weight:500;line-height:1}
.brand-tag{font-size:11px;letter-spacing:2.6px;margin-top:4px}
.nav{position:absolute;top:48px;right:112px;display:flex;gap:26px;color:#fff;font-size:15px;font-weight:500}
.hero h1{position:absolute;left:108px;top:200px;color:#fff;font-family:"Montserrat",sans-serif;font-weight:800;font-size:60px;line-height:74px;letter-spacing:.5px}
.dots{position:absolute;top:614px;left:572px;display:flex;gap:6px}
.dots span{width:15px;height:15px;border-radius:50%;border:2px solid #fff}
.dots span.on{background:#fff}

/* welcome */
.welcome{top:687px;height:586px;background:#fff}
.stat-text{position:absolute;left:136px;top:256px;width:320px;text-align:center;font-size:22px;line-height:31px;color:var(--ink)}
.para{font-size:15.5px;line-height:27.5px;color:var(--body);font-weight:400}

/* services */
.services{top:1273px;height:707px;background:var(--light)}
.service{position:absolute;top:188px;width:300px;text-align:center}
.service svg{display:block;margin:0 auto}
.service h3{font-family:"Lato",sans-serif;font-weight:400;font-size:23px;margin-top:30px;color:var(--ink)}
.service .stat{font-style:italic;font-size:15px;color:var(--body);margin-top:12px}
.service p{font-size:15px;line-height:25px;color:var(--body);margin-top:22px}
.service .more{color:var(--green);font-size:16px;font-weight:500;margin-top:20px;display:block}

/* process */
.process{top:1980px;height:695px;background:linear-gradient(180deg,#1c5d9d 0%,#1a5894 55%,#164d84 100%)}
.step{position:absolute;top:186px;width:260px;text-align:center}
.ring{width:186px;height:186px;margin:0 auto;border:4px solid #fff;border-radius:50%;position:relative;display:flex;align-items:center;justify-content:center}
.num{position:absolute;left:-26px;top:64px;width:50px;height:50px;border-radius:50%;background:var(--blue);border:3px solid #fff;color:#fff;font-size:28px;font-weight:500;display:flex;align-items:center;justify-content:center}
.step p{color:#fff;font-size:15px;line-height:27.5px;margin-top:28px}

/* clients */
.clients{top:2675px;height:487px;background:#fff}
.logo-row{position:absolute;top:203px;left:112px;display:flex;gap:16px}
.client{width:184px;height:89px;border:2px solid var(--line);display:flex;align-items:center;justify-content:center;gap:8px;font-size:22px;font-weight:700;color:#8a8a8a}
.client i{width:16px;height:16px;background:#9a9a9a;display:block}

/* download */
.download{top:3162px;height:470px}
.download-photo{position:absolute;inset:0;background:linear-gradient(110deg,#3b4048 0%,#4d535b 45%,#2c3036 100%)}
.field{position:absolute;height:51px;background:#fff;border:1px solid #ddd;color:#8a8a8a;font-size:15px;padding:0 16px;display:flex;align-items:center}
.badge{position:absolute;left:799px;top:40px;width:296px;height:296px;border-radius:50%;background:#2b2b2b;color:#fff;text-align:center;font-weight:700}

/* testimonials */
.testimonials{top:3632px;height:547px;background:#fff}
.quote{position:absolute;top:197px;width:308px;height:182px;border:2px solid var(--line);padding:22px 16px;text-align:center;font-style:italic;font-size:15.5px;line-height:27px;color:#8a8a8a;font-weight:300}
.quote.active{border-color:#b8d98b}
.author{position:absolute;top:403px;width:340px;text-align:center;font-size:15.5px;line-height:26px;color:var(--body)}
.author b{display:block;color:var(--ink);font-weight:500;font-size:16px}
.arrow{position:absolute;top:276px}

/* contact */
.contact{top:4179px;height:525px;background:var(--light)}
.contact .field{border-color:#cfcfcf}

/* footer */
.footer{top:4704px;height:376px;background:var(--footer);color:#fff}
.footer h4{font-size:16px;font-weight:600;margin-bottom:14px}
.footer li{list-style:none;font-size:15px;line-height:28.5px}
.social{position:absolute;top:313px;display:flex;gap:10px;right:110px}
.social span{width:40px;height:40px;border:2px solid #fff;border-radius:50%}
</style>
</head>
<body>

<header class="hero">
  <div class="hero-photo" role="img" aria-label="Smiling senior executive with grey beard in a suit working at a laptop in a bright office"></div>
  <div class="brand" style="left:112px;top:34px">
    <div class="brand-box"></div>
    <div><div class="brand-name">Bold Harbor</div><div class="brand-tag">STRONGER STARTS SOONER</div></div>
  </div>
  <nav class="nav"><span>Who We Are</span><span>What We Do</span><span>Clients</span><span>Blog</span><span>Resources</span><span>Contact</span></nav>
  <h1>STRONGER<br>STARTS<br>SOONER</h1>
  <a class="btn" style="left:112px;top:448px;width:180px;height:56px;font-size:17px">Get Started</a>
  <div class="dots"><span class="on"></span><span></span><span></span></div>
</header>

<section class="welcome">
  <svg class="abs" style="left:108px;top:67px" width="376" height="376" viewBox="0 0 376 376">
    <circle cx="188" cy="188" r="182" fill="none" stroke="var(--blue)" stroke-width="6"/>
    <path d="M263 22 A182 182 0 0 1 334 80" fill="none" stroke="#d0d0d0" stroke-width="7"/>
    <g fill="var(--green)">
      <circle cx="165" cy="72" r="12"/><circle cx="211" cy="72" r="12"/><circle cx="188" cy="90" r="13"/>
      <path d="M143 118 q22-34 44 0z M189 118 q22-34 44 0z"/>
      <path d="M160 140 q28-44 56 0z"/>
      <path d="M188 146 l5 10 11 1-8 7 3 11-11-6-11 6 3-11-8-7 11-1z"/>
      <path d="M162 150 l3 6 7 1-5 4 2 7-7-4-6 4 2-7-5-4 6-1z"/>
      <path d="M214 150 l3 6 7 1-5 4 2 7-7-4-6 4 2-7-5-4 6-1z"/>
    </g>
  </svg>
  <div class="stat-text" style="left:136px;top:253px">Get done in 100 days<br>what normally takes 6-12<br>months 90% of Bold Harbor<br>clients succeed</div>
  <div class="abs eyebrow" style="left:531px;top:66px">Who We Are</div>
  <h2 class="abs title" style="left:531px;top:100px">Welcome to Bold Harbor</h2>
  <p class="abs para" style="left:531px;top:173px;width:570px">Bold Harbor accelerates leaders and teams to deliver better results faster through critical transitions, leading to short term and lasting success for the leader and the organization.</p>
  <p class="abs para" style="left:531px;top:283px;width:570px">We create leverage when new CEO's and C-Suite executives are tasked with transforming results and there is a need for speed. Using our 100-Day Action Plan process, leaders quickly build a cohesive team, align around strategic, operational and organizational actions, and dramatically accelerate value creation.</p>
  <a class="btn" style="left:531px;top:458px;width:158px;height:56px">Read More</a>
</section>

<section class="services">
  <div class="abs eyebrow center" style="top:62px">What We Do</div>
  <h2 class="abs title center" style="top:100px">Our Services</h2>

  <div class="service" style="left:111px">
    <svg width="150" height="128" viewBox="0 0 150 128" fill="none" stroke-width="4">
      <g stroke="var(--green)"><circle cx="75" cy="18" r="9"/><path d="M75 2v-2M58 10l-4-3M92 10l4-3M60 22h-5M90 22h5"/></g>
      <g stroke="var(--blue)"><circle cx="48" cy="70" r="15"/><circle cx="104" cy="70" r="15"/><path d="M18 126v-10a30 30 0 0 1 60 0v10M74 126v-10a30 30 0 0 1 60 0v10"/></g>
    </svg>
    <h3>Executive Onboarding</h3>
    <div class="stat">40% of new leaders fail</div>
    <p>For executive leaders taking on new roles, the Bold Harbor 100-Day Action Plan process prepares leaders before the start, speeds up assimilation, sets direction, builds the team, accelerates momentum, and delivers results.</p>
    <span class="more">READ MORE</span>
  </div>

  <div class="service" style="left:450px">
    <svg width="150" height="128" viewBox="0 0 150 128" fill="none" stroke-width="4">
      <g stroke="var(--blue)"><circle cx="75" cy="12" r="8"/><path d="M63 36v-4a12 12 0 0 1 24 0v4z"/><circle cx="75" cy="98" r="8"/><path d="M63 122v-4a12 12 0 0 1 24 0v4z"/><circle cx="22" cy="56" r="8"/><path d="M10 80v-4a12 12 0 0 1 24 0v4z"/><circle cx="128" cy="56" r="8"/><path d="M116 80v-4a12 12 0 0 1 24 0v4z"/></g>
      <g stroke="var(--green)"><path d="M42 22a50 50 0 0 0-18 22M108 22a50 50 0 0 1 18 22M24 92a50 50 0 0 0 24 20M126 92a50 50 0 0 1-24 20"/></g>
    </svg>
    <h3>Team Onboarding</h3>
    <div class="stat">80% of M&amp;A fail to boost returns</div>
    <p>For leaders integrating teams post acquisition or re-organization, the Bold Harbor 100 Day Action Plan process gets all players on board with the change and accelerates achievement of cultural and business integration goals.</p>
    <span class="more">READ MORE</span>
  </div>

  <div class="service" style="left:788px">
    <svg width="150" height="128" viewBox="0 0 150 128" fill="none" stroke-width="4">
      <circle cx="75" cy="64" r="44" stroke="var(--blue)"/>
      <path d="M75 36v28h18" stroke="var(--blue)"/>
      <path d="M28 40a56 56 0 0 1 94-10M122 88a56 56 0 0 1-94 10" stroke="var(--green)"/>
      <path d="M116 24l8 6-10 4M34 104l-8-6 10-4" stroke="var(--green)"/>
    </svg>
    <h3>Acceleration &amp; Restart</h3>
    <div class="stat">70% of transformations fall short</div>
    <p>For executives leading through a strategic point of inflection or reinvigorating a stalled team, Bold Harbor programs define the from-to challenge, kickstart a change process and deliver results that stick.</p>
    <span class="more">READ MORE</span>
  </div>
</section>

<section class="process">
  <div class="abs eyebrow center" style="top:60px;color:#fff">How It Works</div>
  <h2 class="abs title center" style="top:95px;color:#fff">100-Day Action Plan process</h2>

  <div class="step" style="left:91px">
    <div class="ring"><span class="num">1</span>
      <svg width="100" height="90" viewBox="0 0 100 90" fill="none" stroke-width="6"><path d="M8 45h40M36 30l16 15-16 15" stroke="#fff"/><circle cx="66" cy="45" r="22" stroke="var(--green)"/><circle cx="66" cy="45" r="9" stroke="var(--green)"/></svg>
    </div>
    <p>Conduct a prep session and develop a 100-Day Action Plan, incorporating multiple inputs and factors.</p>
  </div>
  <div class="step" style="left:344px">
    <div class="ring"><span class="num">2</span>
      <svg width="110" height="90" viewBox="0 0 110 90" fill="var(--green)"><rect x="14" y="18" width="34" height="34" rx="3"/><rect x="58" y="18" width="34" height="34" rx="3"/><circle cx="52" cy="35" r="7"/><g stroke="#fff" stroke-width="3" fill="none"><path d="M20 68h30M44 62l6 6-6 6M90 78H60M66 72l-6 6 6 6"/></g></svg>
    </div>
    <p>Implementation of the plan, aligning the team around a shared purpose and results-focused action plans.</p>
  </div>
  <div class="step" style="left:594px">
    <div class="ring"><span class="num">3</span>
      <svg width="110" height="90" viewBox="0 0 110 90" fill="none" stroke-width="4"><circle cx="84" cy="20" r="10" stroke="var(--green)"/><circle cx="24" cy="70" r="10" stroke="var(--green)"/><path d="M10 20h60M40 45h60M10 45h20M40 70h50" stroke="#fff" stroke-dasharray="6 4"/></svg>
    </div>
    <p>The approach addresses strategic, operational and organizational actions required to deliver early and lasting success.</p>
  </div>
  <div class="step" style="left:843px">
    <div class="ring"><span class="num">4</span>
      <svg width="110" height="100" viewBox="0 0 110 100" fill="none" stroke-width="4"><path d="M20 90V60M34 90V48M48 90V56M62 90V40" stroke="#fff"/><circle cx="24" cy="20" r="9" stroke="var(--green)"/><circle cx="78" cy="26" r="14" stroke="var(--green)"/><path d="M76 40v40l12 12" stroke="#fff"/></svg>
    </div>
    <p>We provide behind-the-scenes coaching and adjust along the way to help our clients deliver stronger results sooner.</p>
  </div>
  <a class="btn" style="left:520px;top:574px;width:160px;height:56px">Get Started</a>
</section>

<section class="clients">
  <div class="abs eyebrow center" style="top:76px">Who We Serve</div>
  <h2 class="abs title center" style="top:112px">Our Clients Have Used Us Over 180 Times</h2>
  <div class="logo-row">
    <div class="client"><i></i>Boxline</div>
    <div class="client">Ridgefield</div>
    <div class="client" style="border-color:#b8d98b">Crimsonway</div>
    <div class="client">Stonebridge</div>
    <div class="client">Vantage</div>
  </div>
  <a class="btn" style="left:395px;top:349px;width:410px;height:61px">View More Our Worldwide Clients</a>
</section>

<section class="download">
  <div class="download-photo" role="img" aria-label="Close-up of hands typing on a laptop keyboard"></div>
  <div class="abs" style="left:110px;top:68px;color:#fff;font-family:'Lato',sans-serif;font-size:23px">Downlod BH</div>
  <h2 class="abs" style="left:110px;top:103px;color:#fff;font-family:'Lato',sans-serif;font-weight:700;font-size:40px">Get Started With A Prep Session</h2>
  <div class="field" style="left:111px;top:184px;width:315px">First Name</div>
  <div class="field" style="left:438px;top:184px;width:315px">Last Name</div>
  <div class="field" style="left:111px;top:253px;width:642px">Email Address</div>
  <a class="btn" style="left:111px;top:338px;width:235px;height:60px">Download Now</a>
  <div class="badge">
    <div style="margin-top:58px;font-size:30px;letter-spacing:1px">DOWNLOAD</div>
    <div style="font-size:84px;line-height:92px;font-weight:800">BH</div>
    <div style="font-size:24px;line-height:27px">100 Day Action<br>Plan Process</div>
  </div>
</section>

<section class="testimonials">
  <div class="abs eyebrow center" style="top:70px">Testimonials</div>
  <h2 class="abs title center" style="top:106px">What Our Clients Say</h2>
  <svg class="arrow" style="left:56px" width="18" height="28" viewBox="0 0 18 28"><path d="M15 2L3 14l12 12" fill="none" stroke="#777" stroke-width="3"/></svg>
  <svg class="arrow" style="left:1124px" width="18" height="28" viewBox="0 0 18 28"><path d="M3 2l12 12L3 26" fill="none" stroke="#777" stroke-width="3"/></svg>
  <div class="quote" style="left:112px">Somewhere right now, there is a first time CEO out there, not working with Bold Harbor, not following their 100-Day Action Plan, and I am worried for them.</div>
  <div class="quote active" style="left:446px">I have worked with Bold Harbor twice in the last 24 months, first as a private equity investor and most recently as a first time leader of a company.</div>
  <div class="quote" style="left:780px">Bold Harbor has helped me successfully transition into a number of different roles, in Corporate and Private Equity settings.</div>
  <div class="author" style="left:96px"><b>Anna Kellerman</b>CEO Quillmoor Integrated Solutions</div>
  <div class="author" style="left:430px"><b>Mark Delaney</b>former Managing Director<br>of Tallowmere Equity Partners</div>
  <div class="author" style="left:764px"><b>Paul Whitford</b>CEO Brackenridge Academies</div>
</section>

<section class="contact">
  <div class="abs eyebrow center" style="top:64px">Get In Touch</div>
  <h2 class="abs title center" style="top:100px">Contact Us</h2>
  <div class="field" style="left:199px;top:183px;width:394px;height:49px">Name</div>
  <div class="field" style="left:199px;top:246px;width:394px;height:49px">Email</div>
  <div class="field" style="left:199px;top:306px;width:394px;height:49px">Phone No</div>
  <div class="field" style="left:610px;top:183px;width:390px;height:172px;align-items:flex-start;padding-top:14px">Message</div>
  <a class="btn" style="left:535px;top:397px;width:130px;height:61px">Send</a>
</section>

<footer class="footer">
  <div class="brand" style="left:112px;top:62px">
    <div class="brand-box"></div>
    <div><div class="brand-name">Bold Harbor</div><div class="brand-tag">STRONGER STARTS SOONER</div></div>
  </div>
  <p class="abs" style="left:110px;top:142px;font-size:16px;line-height:28px">Accelerate Business Performance<br>During Critical Leadership Transitions</p>
  <div class="abs" style="left:549px;top:64px"><h4>Quick Links</h4>
    <ul><li>Home</li><li>Who We Are</li><li>What We Do</li><li>Clients</li><li>Blog</li><li>Contact</li></ul></div>
  <div class="abs" style="left:754px;top:64px"><h4>Contact Us</h4>
    <ul><li>US +1 555.010.2040</li><li>UK +44 (0) 7700 900123</li></ul></div>
  <div class="abs" style="left:110px;top:290px;width:980px;height:1px;background:#555"></div>
  <p class="abs" style="left:110px;top:322px;font-size:15px">© 2021 Bold Harbor | STRONGER STARTS SOONER Since 2003.</p>
  <div class="social" aria-label="Social media links"><span></span><span></span><span></span></div>
</footer>

</body>
</html>
```